Crest of Morning Paddocks Business Cards with logo

Need a creative business card that pops. Colorful but professional. The attached logo should be included. We are a national horse racing partnership so we are in the equine business. Nothing cartoonlike or whimsical.

Target Market(s)

professionals - 40+

Contact Information for Business Card

Maren Dunleavy
Director of Operations
27 Ashbrook Lane
Larkfield, ST. 00142

Phone (555) 555-0147

FX: (555) 555-0192

email: maren@cmpaddocks.example
cmpaddocks.example

Requirements
Must have
• All information above should be on the business card including the website address. Professional yet creative
Nice to have
• an attention grabbing design. not boring. exciting.
Should not have
• cartoon like - whimsical.

```html
<!DOCTYPE html>
<html lang="en">
<head>
<meta charset="utf-8">
<title>Crest of Morning Paddocks – Business Card</title>
<link href="https://fonts.googleapis.com/css2?family=Crimson+Pro:wght@400;600&display=swap" rel="stylesheet">
<style>
  :root {
    --stage: #3f4290;
    --card: #fbfbf9;
    --navy: #2b2f7a;
    --gold: #c99a2e;
    --ink: #2f3275;
  }
  * { margin: 0; padding: 0; box-sizing: border-box; }
  html, body {
    width: 1200px;
    height: 1000px;
    overflow: hidden;
    background: var(--stage);
  }
  .stage {
    width: 1200px;
    height: 1000px;
    display: flex;
    align-items: center;
    justify-content: center;
  }
  .business-card {
    position: relative;
    width: 840px;
    height: 480px;
    background: var(--card);
    box-shadow: 0 18px 40px rgba(10, 12, 50, 0.35);
    font-family: "Crimson Pro", Georgia, serif;
    color: var(--ink);
  }
  .brand {
    position: absolute;
    left: 70px;
    top: 150px;
    width: 330px;
    display: flex;
    align-items: center;
    gap: 20px;
  }
  .brand-circle {
    flex: none;
    width: 44px;
    height: 44px;
    border: 3px solid var(--gold);
    border-radius: 50%;
  }
  .brand-name {
    font-weight: 600;
    font-size: 38px;
    line-height: 1.08;
    letter-spacing: 1px;
    text-transform: uppercase;
    color: var(--navy);
  }
  .contact {
    position: absolute;
    left: 470px;
    top: 108px;
    width: 330px;
  }
  .contact-name {
    font-weight: 600;
    font-size: 34px;
    line-height: 1;
    color: var(--gold);
  }
  .contact-title {
    margin-top: 4px;
    font-size: 15px;
    letter-spacing: 3px;
    text-transform: uppercase;
    color: var(--navy);
  }
  .contact-address {
    margin-top: 18px;
    font-size: 19px;
    line-height: 1.25;
  }
  .contact-lines {
    margin-top: 16px;
    list-style: none;
    font-size: 19px;
    line-height: 1.25;
  }
  .contact-lines .label {
    display: inline-block;
    width: 16px;
    color: var(--gold);
    font-weight: 600;
  }
  .contact-web {
    margin-top: 18px;
    font-size: 19px;
  }
  .contact-web strong {
    color: var(--gold);
    font-weight: 600;
  }
</style>
</head>
<body>
  <main class="stage">
    <section class="business-card">
      <div class="brand">
        <span class="brand-circle"></span>
        <span class="brand-name">Crest of Morning Paddocks</span>
      </div>
      <div class="contact">
        <h1 class="contact-name">Maren Dunleavy</h1>
        <p class="contact-title">Director of Operations</p>
        <p class="contact-address">27 Ashbrook Lane<br>Larkfield, ST. 00142</p>
        <ul class="contact-lines">
          <li><span class="label">P</span> (555) 555-0147</li>
          <li><span class="label">F</span> (555) 555-0192</li>
          <li><span class="label">E</span> maren@cmpaddocks.example</li>
        </ul>
        <p class="contact-web">www.<strong>cmpaddocks</strong>.example</p>
      </div>
    </section>
  </main>
</body>
</html>
```